New Website Deisgn. Guaranteed Project.

I would like a site similar to this: http://givebikeforhope.org.

old site: http://wheelsforrelief.org

Create a professional website; a car donation site seeking leads to return calls.

Please see http://givebikeforhope.org for the concept I am after.

The webpage should have a professional feel. The pages to include are 'Home', 'About us' and 'Get Started'

Industry/Entity Type

It Professional

Coding

Coded - Design and coding required

Number of Pages Required

1 page

```html
<!DOCTYPE html>
<html lang="en">
<head>
<meta charset="utf-8">
<title>Bright Path Kids Foundation – Donate Your Car</title>
<link href="https://fonts.googleapis.com/css2?family=Open+Sans:wght@400;600;700&family=Montserrat:wght@600;700&display=swap" rel="stylesheet">
<style>
:root{
  --red:#e8403f;
  --red-dark:#c9302f;
  --yellow:#f7c531;
  --text:#333;
  --muted:#777;
  --line:#e3e3e3;
  --bg:#f1f1f1;
  --white:#fff;
  --blue:#3b6fc4;
  --green:#4aa54a;
  --orange:#f29a2e;
}
*{box-sizing:border-box;margin:0;padding:0}
html,body{width:870px;height:1200px;overflow:hidden}
body{font-family:"Open Sans",Arial,sans-serif;color:var(--text);background:var(--bg);font-size:10px;position:relative}
.container{width:690px;margin:0 auto;position:relative}

/* header */
.site-header{height:58px;background:var(--white);border-bottom:1px solid var(--line)}
.site-header .container{display:flex;justify-content:space-between;align-items:center;height:58px}
.brand{display:flex;align-items:center;gap:8px;font-family:"Montserrat",sans-serif;font-weight:700;font-size:12px;line-height:1.15;color:var(--red);width:170px}
.brand-dot{width:30px;height:30px;border-radius:50%;background:var(--red);flex:none}
.main-nav{display:flex;height:58px}
.main-nav a{display:flex;align-items:center;padding:0 14px;font-size:8.5px;font-weight:600;color:var(--text);text-decoration:none;text-transform:uppercase;border-left:1px solid var(--line)}
.main-nav a.active{color:var(--red);border-top:3px solid var(--red)}

/* hero */
.hero{height:348px;position:relative}
.hero-photo{position:absolute;inset:0;background:linear-gradient(110deg,#eef0f3 0%,#d9dde2 40%,#c9cdd3 70%,#aeb4bc 100%)}
.donate-panel{position:absolute;right:40px;top:0;width:240px;height:334px;background:var(--red);color:var(--white);padding:16px 16px;text-align:center}
.donate-panel h1{font-family:"Montserrat",sans-serif;font-size:15px;font-weight:700;letter-spacing:.3px}
.donate-panel .tagline{font-size:7.5px;margin-top:3px;text-transform:uppercase;opacity:.9}
.donate-panel .call-box{background:var(--white);color:var(--red);margin:12px 0 12px;padding:8px 0}
.call-box .phone{font-family:"Montserrat",sans-serif;font-size:20px;font-weight:700}
.call-box small{display:block;font-size:7px;color:var(--muted);text-transform:uppercase}
.fields{display:grid;grid-template-columns:1fr 1fr;gap:6px}
.field{background:var(--white);height:20px;font-size:7.5px;color:#999;text-align:left;padding:5px 6px}
.field.wide{grid-column:span 2}
.donate-btn{display:block;margin-top:10px;background:var(--yellow);color:var(--text);font-weight:700;font-size:9px;padding:8px 0;text-transform:uppercase}

/* benefits */
.benefits{background:var(--white);height:160px;border-bottom:1px solid var(--line)}
.benefits ul{list-style:none;display:flex;height:160px;padding:0 40px}
.benefits li{flex:1;display:flex;flex-direction:column;align-items:center;justify-content:center;text-align:center;border-right:1px solid var(--line);padding:0 10px;font-size:8.5px;color:var(--red);line-height:1.35}
.benefits li:last-child{border-right:none}
.benefits svg{width:32px;height:32px;margin-bottom:10px;stroke:var(--red);fill:none;stroke-width:2}

/* welcome */
.welcome{padding:34px 0 0}
.welcome .eyebrow{font-size:9px;font-weight:700;text-transform:uppercase;letter-spacing:.5px}
.welcome h2{font-family:"Montserrat",sans-serif;font-size:17px;color:var(--red);margin-top:4px}
.features{display:grid;grid-template-columns:1fr 1fr;gap:20px 24px;margin-top:32px}
.feature{background:var(--white);height:100px;display:flex;gap:14px;padding:16px;box-shadow:0 1px 2px rgba(0,0,0,.08)}
.feature-icon{width:36px;height:36px;border:2px solid var(--red);border-radius:4px;flex:none;display:flex;align-items:center;justify-content:center}
.feature-icon svg{width:20px;height:20px;stroke:var(--red);fill:none;stroke-width:2}
.feature h3{font-size:10px;font-weight:700;margin-bottom:5px}
.feature p{font-size:7.5px;color:var(--muted);line-height:1.45}

/* footer */
.site-footer{position:absolute;left:0;right:0;top:1030px;background:var(--white);height:105px}
.site-footer .container{display:flex;align-items:center;height:105px;gap:40px}
.footer-menu{flex:1}
.footer-menu h4,.social h4{font-size:8px;text-transform:uppercase;margin-bottom:6px}
.footer-menu nav{font-size:7.5px;color:var(--muted);display:flex;gap:8px}
.social-list{display:flex;gap:5px}
.social-list span{width:14px;height:14px;border-radius:50%;background:var(--blue)}
.copyright{position:absolute;left:0;right:0;top:1135px;text-align:center;font-size:7px;color:var(--muted);padding-top:10px}
</style>
</head>
<body>

<header class="site-header">
  <div class="container">
    <div class="brand"><span class="brand-dot"></span>Bright Path Kids Foundation</div>
    <nav class="main-nav">
      <a href="#" class="active">Home</a>
      <a href="#">Charities</a>
      <a href="#">Donate</a>
      <a href="#">Contact Us</a>
    </nav>
  </div>
</header>

<section class="hero">
  <div class="hero-photo" role="img" aria-label="Photo of a smiling mother and daughter with donated cars in a bright studio"></div>
  <form class="donate-panel">
    <h1>DONATE CAR TO CHARITY!</h1>
    <p class="tagline">Your car can make a difference</p>
    <div class="call-box">
      <div class="phone">1-800-555-0142</div>
      <small>Call today · Donate now</small>
    </div>
    <div class="fields">
      <div class="field">First Name</div>
      <div class="field">Last Name</div>
      <div class="field wide">Phone</div>
      <div class="field wide">E-mail Address</div>
      <div class="field">Year of Car</div>
      <div class="field">Choose Make</div>
      <div class="field">Model of Car</div>
      <div class="field">Zip Code</div>
    </div>
    <span class="donate-btn">Click here to donate now</span>
  </form>
</section>

<section class="benefits">
  <ul>
    <li><svg viewBox="0 0 32 32"><path d="M4 20h24v5H4zM7 20l3-7h12l3 7"/><circle cx="9" cy="26" r="2"/><circle cx="23" cy="26" r="2"/></svg>Car Donations are EASY</li>
    <li><svg viewBox="0 0 32 32"><path d="M3 10h16v12H3zM19 14h6l4 4v4H19z"/><circle cx="9" cy="24" r="2"/><circle cx="24" cy="24" r="2"/></svg>Free Pick Up Nationwide</li>
    <li><svg viewBox="0 0 32 32"><path d="M8 4h16v24H8zM12 10h8M12 15h8M12 20h5"/></svg>Tax Deductible</li>
    <li><svg viewBox="0 0 32 32"><path d="M8 4h16v24H8zM12 12l8 8M20 12l-8 8"/></svg>No Paperwork Hassle</li>
    <li><svg viewBox="0 0 32 32"><path d="M6 6h20v20H6zM11 16l4 4 7-8"/></svg>Donation Free of Trying to Sell a Used Car</li>
    <li><svg viewBox="0 0 32 32"><circle cx="16" cy="16" r="11"/><path d="M16 9v14M20 12h-6a2 2 0 0 0 0 4h4a2 2 0 0 1 0 4h-6"/></svg>Save Money on Car Bills</li>
  </ul>
</section>

<section class="welcome">
  <div class="container">
    <p class="eyebrow">Welcome to</p>
    <h2>Bright Path Kids Foundation</h2>
    <div class="features">
      <article class="feature">
        <div class="feature-icon"><svg viewBox="0 0 20 20"><path d="M2 6h10v8H2zM12 9h4l2 3v2h-6"/></svg></div>
        <div><h3>Free Towing in 24-48 hours (with Tax Receipt)</h3><p>We pick up your car anywhere in the country at no cost and hand you a receipt right at the door so you can claim it later.</p></div>
      </article>
      <article class="feature">
        <div class="feature-icon"><svg viewBox="0 0 20 20"><path d="M4 10l4 4 8-8"/></svg></div>
        <div><h3>We Accept All Cars</h3><p>Running or not, old or new, we welcome every car, truck, van or boat and turn it into support for children.</p></div>
      </article>
      <article class="feature">
        <div class="feature-icon"><svg viewBox="0 0 20 20"><path d="M3 17h14M5 13h10M10 3v10"/></svg></div>
        <div><h3>Car Will Be Sold on the Largest Auction Network</h3><p>Your vehicle goes to a wide buyer network so it earns the best value and the biggest gift for our programs.</p></div>
      </article>
      <article class="feature">
        <div class="feature-icon"><svg viewBox="0 0 20 20"><path d="M10 17s-7-4-7-9a4 4 0 0 1 7-2 4 4 0 0 1 7 2c0 5-7 9-7 9z"/></svg></div>
        <div><h3>Car donations help fund charitable programs</h3><p>Every donation backs care, family help and research for young patients through our registered nonprofit work.</p></div>
      </article>
      <article class="feature">
        <div class="feature-icon"><svg viewBox="0 0 20 20"><path d="M5 2h10v16H5zM8 7h4M8 11h4"/></svg></div>
        <div><h3>Income Tax Deduction</h3><p>Your gift is fully tax deductible and we send all the paperwork you need for your next return.</p></div>
      </article>
      <article class="feature">
        <div class="feature-icon"><svg viewBox="0 0 20 20"><circle cx="10" cy="10" r="7"/><path d="M7 10l2 2 4-4"/></svg></div>
        <div><h3>Hassle Free Donation</h3><p>Call or fill in the form, we handle title, towing and sale so giving takes only a few minutes of your day.</p></div>
      </article>
    </div>
  </div>
</section>

<footer class="site-footer">
  <div class="container">
    <div class="brand"><span class="brand-dot"></span>Bright Path Kids Foundation</div>
    <div class="footer-menu">
      <h4>Menu</h4>
      <nav><span>Home</span><span>How it works</span><span>Tax Deduction</span><span>Contact us</span></nav>
    </div>
    <div class="social">
      <h4>Connect with us</h4>
      <div class="social-list"><span></span><span></span><span></span><span></span><span></span></div>
    </div>
  </div>
</footer>
<p class="copyright">Copyright © 2024 All Rights Reserved.</p>

</body>
</html>
```